VORTALIX.CH UI Contest - design ONE App Store screenshots for a health + fitness app

Vortalix.ch is a tech incubator on a beach in Thailand and we're looking for a superstar UX/UI designer - the winner of this contest will be invited to work with us remotely and will be considered for the full incubator program!
For this contest, you will need to design ONE highly representative screenshot of an Android app. We will take all the submitted screenshots and will then A/B test them in Google Play on a selection of audiences (US M+F 14-45) - the screenshots that have the best conversion rate wins! We then would expect the winner of the content to design the final 2 screenshots for us as part of the contest.
I'm attaching an explanation of how the app works and design considerations in a ppt. The basic idea is that we have developed a mobile app that allows you to accurately track your cardio respiratory health + fitness level, stress levels and cognitive levels from your phone; without any other devices - only using your phone camera. It allows us to see what effect the things that you do in your daily life have on your fitness, cardio, stress and cognitive levels. For example for fitness, we can detect that your fitness level has improved after even 2-3 sessions of walking; while it would take you months to see the results on your body in the gym. We can detect your stress levels increasing before you are starting to get sick and notice it yourself.
We have tested the software in a marathon style event, where we test a group's levels of fitness, stress and cognitive levels then give them recommendations and test them again after a month - whoever improved the most; gets a prize.
Right now, the software acts as a basic tracker, but we are hoping to add recommendations too and that's what will inform the final design. So you set your goals, track your levels for a few days and then we provide recommendations to you, based on other folks successful experiences and on your personal level.
We are very open minded so feel free to experiment – the ideas that we have presented in the doc are not exhaustive so if you have an idea for a better screenshot/app layout/UX/UI or even an entire new concept! – email us and we can tell you if it works with our technology.
Feel free to check out pq7rm.com for an idea of a previous sports oriented app prototype that we made before.
Good luck!
Target Market(s)
Male and Female, US + EU, 14-45 age
We are looking to target people who are suffering from stress, low energy, low fitness. People who are unhappy with the way they look and feel!
Industry/Entity Type
Health And Wellness
Colors
Designer to choose colors to be used in the design.
Requirements
Must have
- Screenshots that depict the phone at least and will work well in attracting target users to download the app - they should be easy to see on a phone screen and should be colourful and appealing - check the ppt.
Nice to have
- For multiple screenshots it would be nice to have a person in the shot to make it more relatable.
Should not have
- No super sexualised images.

```html
<!DOCTYPE html>
<html lang="en">
<head>
<meta charset="utf-8">
<title>Stride Spark – App Design</title>
<link rel="stylesheet" href="https://fonts.googleapis.com/css2?family=Fredoka:wght@400;500;600&family=Montserrat:wght@500;700;800&display=swap">
<style>
  :root{
    --ink:#10202c;
    --navy:#0f2130;
    --navy-deep:#07182a;
    --screen:#1b2b4a;
    --teal:#00bf9a;
    --teal-light:#7fd9c2;
    --lime:#a8d816;
    --yellow:#f5c410;
    --stripe-yellow:#f7e600;
    --blue:#2196f3;
    --pink:#ee3a8c;
    --purple:#c52bd8;
    --red:#e6253a;
    --green:#38d13a;
    --cyan:#14c3d6;
    --grey-text:#4a4a4a;
    --ring-track:#e3e6ea;
    --white:#ffffff;
  }
  *{margin:0;padding:0;box-sizing:border-box}
  html,body{width:1200px;height:1200px;overflow:hidden;background:var(--white)}
  .canvas{position:relative;width:1200px;height:1200px;background:var(--white);font-family:"Fredoka",sans-serif}
  .title{position:absolute;top:34px;left:0;width:100%;text-align:center;font-weight:600;font-size:62px;color:var(--ink);letter-spacing:.5px}
  .subtitle{position:absolute;top:112px;left:0;width:100%;text-align:center;font-weight:400;font-size:35px;color:var(--grey-text)}
  .decor{position:absolute;top:0;left:0}
  .screenshot{position:absolute;width:440px;height:782px;border-radius:18px;overflow:hidden}
  .screenshot--left{left:131px;top:207px}
  .screenshot--right{left:609px;top:212px}
  .screenshot svg{display:block}
  .caption{position:absolute;color:var(--white);font-weight:500}
  .caption--left{left:29px;top:666px;font-size:27px;line-height:40px;width:400px}
  .caption--right{left:30px;top:24px;font-size:23px;line-height:40px;width:400px}
  .app-text{font-family:"Montserrat",sans-serif}
  .chip-label{font-family:"Fredoka",sans-serif}
</style>
</head>
<body>
<div class="canvas">
  <h1 class="title">Stride Spark</h1>
  <p class="subtitle">App Design</p>

  <svg class="decor" width="1200" height="1200" viewBox="0 0 1200 1200" aria-hidden="true">
    <path d="M92 132v20M82 142h20" stroke="var(--pink)" stroke-width="6"/>
    <circle cx="331" cy="142" r="16" fill="none" stroke="var(--purple)" stroke-width="7"/>
    <circle cx="97" cy="330" r="12" fill="none" stroke="var(--yellow)" stroke-width="6"/>
    <path d="M1122 914v30M1107 929h30" stroke="var(--cyan)" stroke-width="8"/>
    <circle cx="910" cy="1045" r="16" fill="none" stroke="var(--red)" stroke-width="7"/>
    <circle cx="1168" cy="1029" r="13" fill="none" stroke="var(--yellow)" stroke-width="6"/>
    <path d="M1077 1070v20M1067 1080h20" stroke="var(--blue)" stroke-width="6"/>
  </svg>

  <section class="screenshot screenshot--left">
    <svg width="440" height="782" viewBox="0 0 440 782">
      <rect width="440" height="782" fill="var(--teal)"/>
      <polygon points="0,0 440,0 440,40 0,210" fill="var(--navy)"/>
      <polygon points="0,210 440,40 440,58 0,228" fill="var(--teal-light)"/>
      <g transform="translate(34,223) rotate(-40)">
        <rect x="-10" y="-10" width="440" height="920" rx="64" fill="#eef1f4"/>
        <rect x="0" y="0" width="420" height="900" rx="56" fill="var(--screen)"/>
        <rect x="30" y="330" width="400" height="600" rx="20" fill="var(--white)"/>
        <text class="app-text" x="40" y="262" fill="var(--white)" font-size="15" font-weight="700">Users with your profile and goals</text>
        <text class="app-text" x="60" y="290" fill="var(--white)" font-size="15" font-weight="700">found success with:</text>
        <rect x="40" y="128" width="360" height="106" rx="16" fill="var(--yellow)"/>
        <circle cx="110" cy="181" r="32" fill="#fde58a"/>
        <circle cx="110" cy="181" r="21" fill="#66d12e"/>
        <circle cx="110" cy="181" r="10" fill="none" stroke="var(--white)" stroke-width="3"/>
        <text class="app-text" x="160" y="165" fill="#fff7c8" font-size="12" font-weight="500">Goals:</text>
        <text class="app-text" x="160" y="188" fill="var(--white)" font-size="15" font-weight="800">• Improve Focus</text>
        <text class="app-text" x="160" y="210" fill="var(--white)" font-size="15" font-weight="800">• Improve Fitness</text>
        <rect x="-70" y="32" width="346" height="110" rx="16" fill="var(--blue)"/>
        <circle cx="-8" cy="87" r="34" fill="#74bdf7"/>
        <circle cx="-8" cy="87" r="22" fill="var(--pink)"/>
        <text class="app-text" x="42" y="74" fill="#d4eaff" font-size="12" font-weight="500">Profile:</text>
        <text class="app-text" x="42" y="98" fill="var(--white)" font-size="16" font-weight="800">Young Adventure Seeker</text>
        <circle cx="134" cy="393" r="56" fill="none" stroke="var(--ring-track)" stroke-width="8"/>
        <circle cx="134" cy="393" r="56" fill="none" stroke="var(--red)" stroke-width="8" stroke-dasharray="338 352" transform="rotate(-90 134 393)"/>
        <rect x="114" y="368" width="36" height="40" rx="6" fill="var(--red)" opacity=".85" role="img" aria-label="Running figure icon"/>
        <text class="app-text" x="150" y="428" fill="var(--red)" font-size="15" font-weight="800">96%</text>
      </g>

      <g class="ai-chip" transform="translate(30,514)">
        <g stroke="var(--white)" stroke-width="4" stroke-linecap="square">
          <path d="M34 10v14M50 10v14M66 10v14M82 10v14"/>
          <path d="M34 106v14M50 106v14M66 106v14M82 106v14"/>
          <path d="M4 42h14M4 58h14M4 74h14M4 90h14"/>
          <path d="M102 42h14M102 58h14M102 74h14M102 90h14"/>
        </g>
        <rect x="20" y="26" width="80" height="78" rx="10" fill="var(--white)"/>
        <polygon points="28,34 44,34 28,50" fill="var(--teal)"/>
        <text class="chip-label" x="82" y="50" text-anchor="middle" fill="var(--teal)" font-size="18" font-weight="600">ai</text>
        <ellipse cx="58" cy="80" rx="26" ry="16" fill="var(--teal)" role="img" aria-label="Brain symbol"/>
      </g>
    </svg>
    <p class="caption caption--left">AI powered recommendation engine tailored to you...</p>
  </section>

  <section class="screenshot screenshot--right">
    <svg width="440" height="782" viewBox="0 0 440 782">
      <rect width="440" height="782" fill="var(--lime)"/>
      <rect width="440" height="134" fill="var(--navy-deep)"/>
      <polygon points="0,132 440,122 440,134 0,146" fill="var(--stripe-yellow)"/>
      <polygon points="0,146 440,134 440,152 0,168" fill="var(--white)"/>
      <g transform="translate(341,253)" fill="none" stroke="var(--white)" stroke-width="11">
        <path d="M-38 -24 A45 45 0 1 1 -40 20"/>
        <path d="M-4 -22 V0 H18" stroke-linecap="round"/>
        <path d="M-52 -34 L-38 -22 L-24 -38" stroke-width="8"/>
      </g>
      <g transform="translate(171,748) rotate(-52)">
        <rect x="-10" y="-770" width="390" height="780" rx="60" fill="#eef1f4"/>
        <rect x="0" y="-760" width="370" height="760" rx="52" fill="var(--screen)"/>
        <rect x="14" y="-720" width="342" height="644" rx="20" fill="var(--white)"/>
        <g class="app-text" font-weight="800" font-size="14" text-anchor="middle">
          <circle cx="100" cy="-360" r="55" fill="none" stroke="var(--ring-track)" stroke-width="8"/>
          <circle cx="100" cy="-360" r="55" fill="none" stroke="var(--red)" stroke-width="8" stroke-dasharray="300 346" transform="rotate(-90 100 -360)"/>
          <text x="100" y="-280" fill="var(--ink)" font-size="16">Run</text>

          <circle cx="280" cy="-360" r="55" fill="none" stroke="var(--ring-track)" stroke-width="8"/>
          <circle cx="280" cy="-360" r="55" fill="none" stroke="var(--purple)" stroke-width="8" stroke-dasharray="259 346" transform="rotate(-90 280 -360)"/>
          <rect x="262" y="-382" width="34" height="30" rx="6" fill="var(--purple)" opacity=".8" role="img" aria-label="Yoga pose icon"/>
          <text x="288" y="-330" fill="var(--purple)">75%</text>
          <text x="280" y="-280" fill="var(--ink)" font-size="16">Yoga</text>

          <circle cx="280" cy="-190" r="55" fill="none" stroke="var(--ring-track)" stroke-width="8"/>
          <circle cx="280" cy="-190" r="55" fill="none" stroke="var(--green)" stroke-width="8" stroke-dasharray="60 346" transform="rotate(-90 280 -190)"/>
          <rect x="262" y="-213" width="36" height="32" rx="6" fill="var(--green)" opacity=".8" role="img" aria-label="Crossfit athletes icon"/>
          <text x="290" y="-161" fill="var(--green)">75%</text>
          <text x="280" y="-108" fill="var(--ink)" font-size="16">Crossfit</text>

          <circle cx="100" cy="-190" r="55" fill="none" stroke="var(--ring-track)" stroke-width="8"/>
          <circle cx="100" cy="-190" r="55" fill="none" stroke="var(--blue)" stroke-width="8" stroke-dasharray="131 346" transform="rotate(-90 100 -190)"/>
          <rect x="82" y="-213" width="34" height="32" rx="6" fill="var(--blue)" opacity=".8" role="img" aria-label="Meditation pose icon"/>
          <text x="108" y="-161" fill="var(--blue)">38%</text>
          <text x="100" y="-108" fill="var(--ink)" font-size="16">Meditate</text>
        </g>
        <g fill="none" stroke="var(--white)" stroke-width="2.5" stroke-linecap="round" stroke-linejoin="round">
          <path d="M80 -38 h16 M86 -44 l-6 6 6 6"/>
          <rect x="176" y="-46" width="18" height="16" rx="2"/>
          <path d="M276 -44 l-8 8 h12 M286 -32 l8 -8 h-12"/>
        </g>
      </g>
    </svg>
    <p class="caption caption--right">...and based on past users sucess rates.</p>
  </section>
</div>
</body>
</html>
```